Submittal Letter - Letterhead

want something that matches our colors that looks professional for a design build engineering fan. Feel Free to incorporate Engineering, Procurement, Construction and Maintenance as a tagline type heading if it makes sense.

```html
<!DOCTYPE html>
<html lang="en">
<head>
<meta charset="utf-8">
<title>Harlan Reed – Submittal Letter Letterhead</title>
<link href="https://fonts.googleapis.com/css2?family=Barlow:wght@400;500;700&family=Montserrat:wght@700&display=swap" rel="stylesheet">
<style>
  :root {
    --brand-red: #d52b35;
    --brand-black: #0d0d0d;
    --ink: #222222;
    --paper: #ffffff;
    --backdrop: #e4e4e4;
  }
  html, body {
    margin: 0;
    padding: 0;
    width: 1200px;
    height: 1200px;
    overflow: hidden;
    background: var(--backdrop);
  }
  .letterhead {
    position: absolute;
    left: 176px;
    top: 0;
    width: 848px;
    height: 1200px;
    background: var(--paper);
    color: var(--ink);
    font-family: "Barlow", Arial, sans-serif;
  }
  .brand {
    position: absolute;
    left: 56px;
    top: 96px;
    display: flex;
    align-items: center;
    gap: 10px;
  }
  .brand-dot {
    width: 26px;
    height: 26px;
    border-radius: 50%;
    background: var(--brand-red);
  }
  .brand-name {
    font-size: 30px;
    font-weight: 700;
    color: var(--brand-black);
    letter-spacing: 0.5px;
  }
  .services {
    position: absolute;
    right: 81px;
    top: 70px;
    margin: 0;
    padding: 0;
    list-style: none;
    text-align: right;
    font-size: 13px;
    line-height: 20px;
    letter-spacing: 0.3px;
  }
  .services li::after {
    content: "";
    display: inline-block;
    width: 6px;
    height: 6px;
    margin-left: 6px;
    border-radius: 50%;
    background: var(--brand-red);
    vertical-align: 1px;
  }
  .recipient {
    position: absolute;
    left: 80px;
    top: 270px;
    margin: 0;
    font-size: 16px;
    line-height: 19px;
    font-style: normal;
    letter-spacing: 0.2px;
  }
  .salutation {
    position: absolute;
    left: 80px;
    top: 400px;
    margin: 0;
    font-size: 16px;
    letter-spacing: 0.2px;
  }
  .letter-body {
    position: absolute;
    left: 80px;
    top: 449px;
    width: 690px;
    font-size: 16.2px;
    line-height: 25.7px;
    letter-spacing: 0.15px;
  }
  .letter-body p { margin: 0; }
  .signatory {
    position: absolute;
    left: 76px;
    top: 930px;
    margin: 0;
    font-family: "Montserrat", Arial, sans-serif;
    font-weight: 700;
    font-size: 13px;
    letter-spacing: 2.4px;
  }
  .signature {
    position: absolute;
    left: 77px;
    top: 947px;
    width: 248px;
    height: 66px;
    background: linear-gradient(90deg, #f2f2f2, #fafafa);
  }
  .sender {
    position: absolute;
    left: 77px;
    top: 1066px;
    font-size: 13.5px;
    line-height: 17px;
  }
  .contact {
    position: absolute;
    left: 77px;
    margin: 0;
    font-size: 15px;
    display: flex;
    align-items: center;
    gap: 5px;
  }
  .contact svg { width: 10px; height: 10px; }
  .contact.phone { top: 1110px; }
  .contact.web { top: 1131px; }
  .footer-band {
    position: absolute;
    left: 0;
    bottom: 2px;
  }
</style>
</head>
<body>
<main class="letterhead">
  <div class="brand">
    <span class="brand-dot"></span>
    <span class="brand-name">Harlan Reed</span>
  </div>

  <ul class="services">
    <li>ENGINEERING</li>
    <li>PROCUREMENT</li>
    <li>CONSTRUCTION</li>
    <li>MAINTENANCE</li>
  </ul>

  <address class="recipient">
    Ms. Laura Whitfield<br>
    Senior Contract Administrator<br>
    Coastal Valley Transit Authority (CVTA)<br>
    410 North Grove Street<br>
    Fairview, California 92801
  </address>

  <p class="salutation">Dear :</p>

  <div class="letter-body">
    <p>Harlan Reed, Inc. (HRI) is pleased to submit our response to Request for Qualifications (RFQ) No. 7-3105 issued by the Coastal Valley Transit Authority (CVTA) for the Design-Build of the Hydrogen Fueling Station and Facility Modifications at Linden Park Bus Base. We appreciate the opportunity to showcase our expertise and are eager to contribute to this important project in support of CVTA’s commitment to sustainable transportation solutions.</p>
    <p>As a corporation organized under the laws of California and authorized to conduct business within the state, we have thoroughly reviewed the RFQ. Enclosed in the forms section are our completed documents, including Form A - Letter of Transmittal and Certification, Form B - Contact Information, and Form C - Addenda Acknowledgement. We have also included a declaration regarding any actual or potential conflicts of interest related to this RFQ. Daniel Mercer serves as the Owner and General Manager of HRI, and he is the primary contact for this submission. Additional main points of contact include Paul Hensley, Director of Engineering (email: phensley@hrinc.com, phone: (555) 019-2734), and Owen Castillo, CFO (email: ocastillo@hrinc.com, phone: (555) 014-8820).</p>
    <p>HRI agrees to keep our submittal, including proposed fees, open for one hundred eighty (180) days. We understand that our submission constitutes a binding offer to provide the services outlined in the RFQ, and we acknowledge that CVTA is not obligated to accept any submission. All costs incurred in the preparation of this submittal will be borne solely by HRI.</p>
  </div>

  <p class="signatory">JONATHAN DOE</p>
  <div class="signature" role="img" aria-label="Handwritten signature of Jonathan Doe"></div>

  <div class="sender">
    1450 Meridian Avenue<br>
    Lakeview, CA 90642
  </div>
  <p class="contact phone">
    <svg viewBox="0 0 10 10" aria-hidden="true"><path d="M2 1 L4 1 L4.6 3 L3.4 3.8 Q4.4 5.8 6.2 6.6 L7 5.4 L9 6 L9 8 Q8 9 6.5 8.8 Q2.5 7.5 1.2 3.5 Q1 2 2 1 Z" fill="var(--brand-red)"/></svg>
    (800) 555-0147
  </p>
  <p class="contact web">
    <svg viewBox="0 0 10 10" aria-hidden="true"><circle cx="5" cy="5" r="4.2" fill="none" stroke="var(--brand-red)" stroke-width="0.9"/><ellipse cx="5" cy="5" rx="1.8" ry="4.2" fill="none" stroke="var(--brand-red)" stroke-width="0.8"/><line x1="0.8" y1="5" x2="9.2" y2="5" stroke="var(--brand-red)" stroke-width="0.8"/></svg>
    www.hrinc.com
  </p>

  <svg class="footer-band" width="848" height="24" viewBox="0 0 848 24" aria-hidden="true">
    <polygon points="0,0 290,0 276,24 0,24" fill="var(--brand-black)"/>
    <polygon points="298,0 848,0 848,24 284,24" fill="var(--brand-red)"/>
  </svg>
</main>
</body>
</html>
```